Icon and Artwork for Cloud Storage Zelvo Application

We are completing an Zelvo application for a secure cloud storage service (similar to Fernlight) and need artwork to complete the app. We would like your help with delivering the following three items:

1. An application icon. This needs to be appropriate for use in the app store (1024x1024 pixels). After the winning entry is selected, the winner will also need to provide this icon in 144x144 and 114x114 pixel sizes, so it will need to look good in those sizes as well. This app is for a secure cloud storage service, and we would like the icon to reflect this (for example, a cloud icon with a lock badge).

2. Login screen. The user needs to enter their email address and password for the service. They should also be able to sign up for a new account from this screen. Ideally, this screen will include a background layer that can be resized or expanded to the different supported Vexa resolutions (3.5", 4", Quorin, Quorin mini).

3. Main screen. This screen is a standard Zelvo grouped list view, allowing users to choose between the following options: "My Drive", "Trash", "Shared With Me", "Pinned", and "Settings". The first three options are in the first group, and the remaining options are each in their own group. There is also a navigation bar with an upload button. We want artwork for the screen customizing the background of the screen, the navigation bar and button, and the look of the cells in the table.

Screens should be submitted in unflattened PSD format.

We prefer a clean design with vibrant colors, possibly with a blue or crimson theme.

Please message me for details including the name of the service.

Thank you for helping with this project!

Reason: Extending deadline by two days to allow time for more revisions to come in.

Reason: Extending deadline to allow time for final designs.

• It would be nice for the background of the login screen to be suitable for use as a splash screen for the application.

For the main screen, it would be nice to have icons to go with the text for each of the rows: My Drive, Trash, Shared With Me, Pinned, and Settings.

```html
<!DOCTYPE html>
<html lang="en">
<head>
<meta charset="utf-8">
<title>Zelvo Cloud Storage – Main Screen</title>
<link rel="stylesheet" href="https://fonts.googleapis.com/css2?family=Lobster+Two:ital,wght@1,700&family=Open+Sans:wght@400;600&family=Arimo:wght@400;700&display=swap">
<style>
:root{
  --page:#e9edf1;
  --status-top:#f4f4f4;
  --status-bottom:#c9c9c9;
  --nav-top:#c9dd86;
  --nav-bottom:#9cbf3f;
  --nav-line:#7c9a2c;
  --content:#e3f0f6;
  --content-dot:#d2e6ef;
  --cell-top:#ffffff;
  --cell-bottom:#e9eef2;
  --cell-border:#c8d3da;
  --divider:#d3dbe1;
  --title:#2d6fb2;
  --title-light:#5a9ad6;
  --sub:#4a4a4a;
  --chevron:#595d62;
  --upload-top:#ffad3a;
  --upload-bottom:#f07a0c;
  --upload-edge:#c95e05;
  --tab-top:#1f3556;
  --tab-bottom:#0f1f38;
  --tab-divider:#2d4468;
  --tab-icon:#6c84ad;
  --tab-active:#a8c934;
  --icon-blue:#5b8fcf;
}
*{margin:0;padding:0;box-sizing:border-box}
html,body{width:1200px;height:2263px;overflow:hidden;background:var(--page)}
.screen{position:absolute;left:38px;top:290px;width:1124px;height:1684px;overflow:hidden;background:var(--content);
  background-image:radial-gradient(var(--content-dot) 3px,transparent 3.5px);background-size:14px 14px;
  box-shadow:0 10px 40px rgba(0,0,0,.18)}
.status-bar{position:absolute;left:0;top:0;width:100%;height:70px;
  background:linear-gradient(var(--status-top),var(--status-bottom));
  font-family:"Arimo",sans-serif;font-size:40px;color:#222;display:flex;align-items:center;padding:0 24px}
.carrier{display:flex;align-items:center;gap:14px}
.clock{position:absolute;left:0;right:0;text-align:center;font-weight:700}
.battery{margin-left:auto}
.nav-bar{position:absolute;left:0;top:70px;width:100%;height:213px;
  background:linear-gradient(var(--nav-top),var(--nav-bottom));border-bottom:3px solid var(--nav-line)}
.app-icon{position:absolute;left:66px;top:42px;width:140px;height:140px;border-radius:14px;
  background:linear-gradient(#9fc1ea,var(--icon-blue));border:4px solid #e8f0fa}
.upload-button{position:absolute;left:413px;top:42px;width:592px;height:144px;border-radius:18px;
  background:linear-gradient(var(--upload-top),var(--upload-bottom));border:3px solid var(--upload-edge);
  box-shadow:inset 0 3px 0 rgba(255,255,255,.45);display:flex;align-items:center;justify-content:space-between;padding:0 40px 0 80px}
.upload-label{font-family:"Lobster Two",cursive;font-style:italic;font-weight:700;font-size:66px;color:#fff}
.group{position:absolute;left:35px;width:1054px;border:3px solid var(--cell-border);border-radius:28px;overflow:hidden;
  background:linear-gradient(var(--cell-top),var(--cell-bottom));box-shadow:0 3px 6px rgba(0,0,0,.08)}
.group-main{top:332px;height:690px}
.group-pinned{top:1054px;height:182px}
.group-settings{top:1271px;height:182px}
.cell{position:relative;height:228px;display:flex;align-items:center;padding-left:70px;
  background:linear-gradient(var(--cell-top),var(--cell-bottom))}
.cell+.cell{border-top:3px solid var(--divider)}
.group-pinned .cell,.group-settings .cell{height:176px}
.cell-text{display:flex;flex-direction:column}
.cell-title{font-family:"Lobster Two",cursive;font-style:italic;font-weight:700;font-size:84px;line-height:1;
  color:var(--title);background:linear-gradient(var(--title-light),var(--title));-webkit-background-clip:text;background-clip:text;-webkit-text-fill-color:transparent}
.cell-sub{font-family:"Open Sans",sans-serif;font-size:33px;color:var(--sub);margin-top:10px}
.cell-icon{position:absolute;right:150px;top:50%;width:140px;height:130px;transform:translateY(-50%);border-radius:18px}
.group-pinned .cell-icon,.group-settings .cell-icon{right:150px}
.icon-drive{background:linear-gradient(#f3f3f3,#a9adb2)}
.icon-trash{background:linear-gradient(#e8eef0,#8fa9a0)}
.icon-shared{background:linear-gradient(#7bcf6a,#3d8fc6)}
.icon-pin{background:linear-gradient(#f6b04a,#d9481c)}
.icon-settings{background:linear-gradient(#e4e4e4,#8a8c8f)}
.chevron{position:absolute;right:40px;top:50%;transform:translateY(-50%)}
.tab-bar{position:absolute;left:0;top:1502px;width:100%;height:182px;display:flex;
  background:linear-gradient(var(--tab-top),var(--tab-bottom))}
.tab{flex:1;display:flex;align-items:center;justify-content:center}
.tab+.tab{border-left:3px solid var(--tab-divider)}
</style>
</head>
<body>
<main class="screen">
  <header class="status-bar">
    <span class="carrier">Kestra-UK
      <svg width="44" height="34" viewBox="0 0 44 34"><path d="M4 12a26 26 0 0 1 36 0M10 19a17 17 0 0 1 24 0M16 26a8 8 0 0 1 12 0" stroke="#2a6fd0" stroke-width="4" fill="none" stroke-linecap="round"/><circle cx="22" cy="31" r="3" fill="#2a6fd0"/></svg>
      <svg width="36" height="36" viewBox="0 0 36 36"><g stroke="#444" stroke-width="4" stroke-linecap="round"><path d="M18 3v8M18 25v8M3 18h8M25 18h8M7 7l6 6M23 23l6 6M29 7l-6 6M13 23l-6 6"/></g></svg>
    </span>
    <span class="clock">08:17</span>
    <svg class="battery" width="70" height="34" viewBox="0 0 70 34"><rect x="2" y="2" width="60" height="30" rx="4" fill="none" stroke="#333" stroke-width="3"/><rect x="63" y="11" width="5" height="12" fill="#333"/><rect x="7" y="7" width="50" height="20" fill="#3fb23a"/></svg>
  </header>

  <nav class="nav-bar">
    <div class="app-icon" role="img" aria-label="App icon: cloud with padlock"></div>
    <div class="upload-button">
      <span class="upload-label">Upload</span>
      <svg width="170" height="110" viewBox="0 0 170 110"><path d="M40 96a32 32 0 0 1 -4-64a42 42 0 0 1 80-8a36 36 0 0 1 18 72z" fill="#fff"/><path d="M85 88V48M65 64l20-22 20 22" stroke="var(--upload-bottom)" stroke-width="12" fill="none" stroke-linecap="round" stroke-linejoin="round"/></svg>
    </div>
  </nav>

  <section class="group group-main">
    <div class="cell">
      <div class="cell-text"><span class="cell-title">My Drive</span><span class="cell-sub">Is a data storage device</span></div>
      <div class="cell-icon icon-drive" role="img" aria-label="Hard drive icon"></div>
      <svg class="chevron" width="34" height="54" viewBox="0 0 34 54"><path d="M6 6l20 21-20 21" stroke="var(--chevron)" stroke-width="9" fill="none"/></svg>
    </div>
    <div class="cell">
      <div class="cell-text"><span class="cell-title">Trash</span><span class="cell-sub">Deleted, unnecessary files</span></div>
      <div class="cell-icon icon-trash" role="img" aria-label="Recycle bin icon"></div>
      <svg class="chevron" width="34" height="54" viewBox="0 0 34 54"><path d="M6 6l20 21-20 21" stroke="var(--chevron)" stroke-width="9" fill="none"/></svg>
    </div>
    <div class="cell">
      <div class="cell-text"><span class="cell-title">Shared with Me</span><span class="cell-sub">Files that are shared with me</span></div>
      <div class="cell-icon icon-shared" role="img" aria-label="Shared files icon"></div>
      <svg class="chevron" width="34" height="54" viewBox="0 0 34 54"><path d="M6 6l20 21-20 21" stroke="var(--chevron)" stroke-width="9" fill="none"/></svg>
    </div>
  </section>

  <section class="group group-pinned">
    <div class="cell">
      <div class="cell-text"><span class="cell-title">Pinned</span></div>
      <div class="cell-icon icon-pin" role="img" aria-label="Push pin icon"></div>
    </div>
  </section>

  <section class="group group-settings">
    <div class="cell">
      <div class="cell-text"><span class="cell-title">Settings</span></div>
      <div class="cell-icon icon-settings" role="img" aria-label="Gears icon"></div>
    </div>
  </section>

  <footer class="tab-bar">
    <div class="tab">
      <svg width="100" height="96" viewBox="0 0 100 96"><path d="M50 4l13 30 33 3-25 22 8 33-29-18-29 18 8-33L4 37l33-3z" fill="var(--tab-icon)"/></svg>
    </div>
    <div class="tab">
      <svg width="110" height="110" viewBox="0 0 110 110"><circle cx="66" cy="42" r="28" fill="none" stroke="var(--tab-active)" stroke-width="11"/><path d="M45 64L12 98" stroke="var(--tab-active)" stroke-width="16" stroke-linecap="round"/></svg>
    </div>
    <div class="tab">
      <svg width="104" height="100" viewBox="0 0 104 100"><g fill="none" stroke="var(--tab-icon)" stroke-width="12" stroke-linejoin="round"><path d="M36 30L52 8l14 22"/><path d="M82 50l12 24H66"/><path d="M36 86H12l12-24"/></g><g fill="var(--tab-icon)"><path d="M62 18l14-6 0 18z"/><path d="M60 88l-10 10 0-20z"/><path d="M18 48l-8-12 18 2z"/></g></svg>
    </div>
  </footer>
</main>
</body>
</html>
```